Worksheet for a seminar - wheel of wellbeing

I need a 1 page worksheet for a course I am running next week.
1. The worksheet is based is designed to tie into Valdoric who use 4 colours per specific quadrants - Blue top left, Yellow top right, Green bottom left, Red bottom right. As this is designed to be written and to be printed, it may need to be pale colours however I am open to the correct colours with the image on top if necessary

2. The wellbeing wheel needs to be a design of it's own as it will be used in other things. I would like to have a format for the base wheel that can be changed by me (Only the title names)

3. I have provided the 2 business logo's - these down need to be too big

I hope this helps.

Target Market(s)

Corporate managers and staff - worksheet being used in a workshop

Industry/Entity Type

Wheel

Colors

Designer to choose colors to be used in the design.

Requirements
Must have
• A professional looking wheel that can be used for other purposes. I want to be able to change the 'pie' titles. I will also require a A4 size of the wheel with blank spaces for titles
Nice to have
• A modern feel

```html
<!DOCTYPE html>
<html lang="en">
<head>
<meta charset="utf-8">
<title>Wheel of Wellbeing Worksheet</title>
<link href="https://fonts.googleapis.com/css2?family=Lato:wght@400;700;900&display=swap" rel="stylesheet">
<style>
  :root {
    --bg: #ececec;
    --paper: #ffffff;
    --band: #e8e8e8;
    --title-blue: #1a75c4;
    --accent-red: #e3161b;
    --ink: #333333;
    --green: #7fb539;
    --red: #f21515;
    --badge: #6b6b6b;
    --field-tail: #e2e2e2;
    --brand-teal: #3aa88a;
    --brand-green: #6fb43a;
    --b1: #0d4677; --b2: #1a5f9e; --b3: #2272b8; --b4: #2f86cf;
    --b5: #3a95dc; --b6: #4aa6e6; --b7: #6bbcf2; --b8: #8dcff8;
    --y1: #d4b71f; --y2: #ddc22a; --y3: #e6ca2e; --y4: #f0d432;
    --y5: #f5de3c; --y6: #fbe56a; --y7: #fbe787; --y8: #fff3b0;
  }
  * { box-sizing: border-box; margin: 0; padding: 0; }
  html, body { width: 1200px; height: 1200px; overflow: hidden; }
  body { background: var(--bg); font-family: 'Lato', sans-serif; color: var(--ink); position: relative; }
  .worksheet {
    position: absolute; left: 185px; top: 20px; width: 829px; height: 1160px;
    background: var(--paper); box-shadow: 0 2px 10px rgba(0,0,0,.12); overflow: hidden;
  }
  .worksheet > * { position: absolute; }
  .title { top: 24px; width: 100%; text-align: center; font-weight: 900; font-size: 50px; color: var(--title-blue); letter-spacing: -0.5px; line-height: 1; }
  .subtitle { top: 79px; width: 100%; text-align: center; font-weight: 400; font-size: 38px; color: var(--accent-red); line-height: 1; }
  .column-label { top: 144px; font-size: 15px; font-weight: 700; color: #3a3a3a; white-space: nowrap; transform: translateX(-50%); }
  .column-label.now { left: 204px; }
  .column-label.goal { left: 622px; }
  .wheel-band { top: 175px; left: 0; width: 100%; height: 374px; background: var(--band); }
  .band-divider { top: 188px; left: 401px; width: 4px; height: 348px; background: linear-gradient(to right, rgba(0,0,0,.12), rgba(0,0,0,0)); }
  .wheel { width: 340px; height: 340px; top: 193px; }
  .wheel.now { left: 32px; }
  .wheel.goal { left: 454px; }
  .wheel text { font-family: 'Lato', sans-serif; font-size: 13px; fill: #fff; text-anchor: middle; }
  .date-label { top: 566px; font-size: 16px; font-weight: 700; color: #2f2f2f; }
  .date-label.start { left: 93px; }
  .date-label.end { left: 481px; }
  .action-panel { top: 607px; left: 0; width: 414px; height: 409px; background: var(--green); }
  .reflect-panel { top: 607px; left: 425px; width: 404px; height: 409px; background: var(--red); }
  .panel-heading { font-size: 14px; font-weight: 700; color: #fff; position: absolute; white-space: nowrap; }
  .action-row { position: absolute; left: 47px; width: 333px; height: 47px; }
  .action-row text { font-family: 'Lato', sans-serif; font-weight: 700; font-size: 27px; fill: #fff; text-anchor: middle; }
  .prompt { position: absolute; left: 62px; width: 290px; font-size: 13.5px; font-weight: 700; color: #fff; line-height: 1.25; }
  .answer-field { position: absolute; left: 59px; width: 290px; height: 42px; }
  .brand { top: 1062px; font-size: 28px; font-weight: 700; line-height: 1; white-space: nowrap; display: flex; align-items: center; gap: 10px; transform: translateX(-50%); }
  .brand .dot { width: 18px; height: 18px; border-radius: 50%; background: currentColor; }
  .brand.wellness { left: 255px; color: var(--brand-teal); }
  .brand.ventures { left: 560px; color: var(--brand-green); }
  .footer-rule { left: 0; bottom: 0; width: 100%; height: 8px; background: var(--green); }
</style>
</head>
<body>
<main class="worksheet">
  <h1 class="title">WHEEL OF WELLBEING</h1>
  <p class="subtitle">a whole brain approach</p>
  <p class="column-label now">Assess where are you now</p>
  <p class="column-label goal">Outcomes Goals&nbsp; where do you want to be?</p>

  <div class="wheel-band"></div>
  <div class="band-divider"></div>

  <svg class="wheel now" viewBox="-170 -170 340 340" aria-label="Wellbeing wheel, current assessment">
    <defs>
      <path id="segment" d="M -59.1 -154 A 165 165 0 0 1 59.1 -154 L 28.7 -74.7 A 80 80 0 0 0 -28.7 -74.7 Z"/>
    </defs>
    <g transform="rotate(20)"><use href="#segment" fill="var(--b2)"/><text y="-126">Physical</text><text y="-110">health</text></g>
    <g transform="rotate(65)"><use href="#segment" fill="var(--b3)"/><text y="-126">Emotional</text><text y="-110">Health</text></g>
    <g transform="rotate(110)"><use href="#segment" fill="var(--b4)"/><text y="-113">Spritual</text></g>
    <g transform="rotate(155)"><use href="#segment" fill="var(--b5)"/><text y="-126">Love</text><text y="-110">Relationship</text></g>
    <g transform="rotate(200)"><use href="#segment" fill="var(--b6)"/><text y="-113">Family</text></g>
    <g transform="rotate(245)"><use href="#segment" fill="var(--b7)"/><text y="-113">Social</text></g>
    <g transform="rotate(290)"><use href="#segment" fill="var(--b8)"/><text y="-126">Personal</text><text y="-110">Growth</text></g>
    <g transform="rotate(335)"><use href="#segment" fill="var(--b1)"/><text y="-134">Business</text><text y="-119">Career</text><text y="-104">study</text></g>
  </svg>

  <svg class="wheel goal" viewBox="-170 -170 340 340" aria-label="Wellbeing wheel, goals">
    <use href="#segment" fill="var(--y2)" transform="rotate(20)"/>
    <use href="#segment" fill="var(--y3)" transform="rotate(65)"/>
    <use href="#segment" fill="var(--y4)" transform="rotate(110)"/>
    <use href="#segment" fill="var(--y5)" transform="rotate(155)"/>
    <use href="#segment" fill="var(--y6)" transform="rotate(200)"/>
    <use href="#segment" fill="var(--y7)" transform="rotate(245)"/>
    <use href="#segment" fill="var(--y8)" transform="rotate(290)"/>
    <use href="#segment" fill="var(--y1)" transform="rotate(335)"/>
  </svg>

  <p class="date-label start">DATE:</p>
  <p class="date-label end">DATE ACHIVED BY:</p>

  <section class="action-panel">
    <p class="panel-heading" style="left:137px;top:24px;">Action Plan Action</p>
    <p class="panel-heading" style="left:309px;top:24px;">When</p>
    <svg class="action-row" style="top:60px" viewBox="0 0 333 47"><rect x="77" y="2" width="175" height="43" fill="#fff"/><polygon points="250,2 310,2 333,23.5 310,45 250,45" fill="var(--field-tail)"/><rect x="0" y="0" width="77" height="47" rx="3" fill="var(--badge)"/><text x="38" y="33">1</text></svg>
    <svg class="action-row" style="top:147px" viewBox="0 0 333 47"><rect x="77" y="2" width="175" height="43" fill="#fff"/><polygon points="250,2 310,2 333,23.5 310,45 250,45" fill="var(--field-tail)"/><rect x="0" y="0" width="77" height="47" rx="3" fill="var(--badge)"/><text x="38" y="33">2</text></svg>
    <svg class="action-row" style="top:241px" viewBox="0 0 333 47"><rect x="77" y="2" width="175" height="43" fill="#fff"/><polygon points="250,2 310,2 333,23.5 310,45 250,45" fill="var(--field-tail)"/><rect x="0" y="0" width="77" height="47" rx="3" fill="var(--badge)"/><text x="38" y="33">3</text></svg>
    <svg class="action-row" style="top:328px" viewBox="0 0 333 47"><rect x="77" y="2" width="175" height="43" fill="#fff"/><polygon points="250,2 310,2 333,23.5 310,45 250,45" fill="var(--field-tail)"/><rect x="0" y="0" width="77" height="47" rx="3" fill="var(--badge)"/><text x="38" y="33">4</text></svg>
  </section>

  <section class="reflect-panel">
    <p class="prompt" style="top:23px">Reflect Are they any surprised in your wheel</p>
    <svg class="answer-field" style="top:53px" viewBox="0 0 290 42"><polygon points="0,0 262,0 290,21 262,42 0,42" fill="#fff"/></svg>
    <p class="prompt" style="top:107px">what wellbeing being gaps stand out as being mood important</p>
    <svg class="answer-field" style="top:148px" viewBox="0 0 290 42"><polygon points="0,0 262,0 290,21 262,42 0,42" fill="#fff"/></svg>
    <p class="prompt" style="top:207px">How do you feel about it?</p>
    <svg class="answer-field" style="top:244px" viewBox="0 0 290 42"><polygon points="0,0 262,0 290,21 262,42 0,42" fill="#fff"/></svg>
    <p class="prompt" style="top:304px">How might this affect your homelife/worklife</p>
    <svg class="answer-field" style="top:333px" viewBox="0 0 290 42"><polygon points="0,0 262,0 290,21 262,42 0,42" fill="#fff"/></svg>
  </section>

  <p class="brand wellness"><span class="dot"></span>Steadfield Wellness</p>
  <p class="brand ventures">Northbrook Ventures</p>
  <div class="footer-rule"></div>
</main>
</body>
</html>
```